Nordic Forgecraft Guild Wordpress Theme and newsletter template

We at the NFG are looking to start a Wordpress website and also send out a newsletter (web). We have just completed a Logo design project with ArtMarketo and we were so pleased with the results that we would like to see what the designers can come up with for a Wordpress theme and a template for an online newsletter. The theme has to support Icelandic letters. It also has to have a subscription option by email. We would need to have the option to add advertisement banners. The theme has to be easy to work with.
Below we have added a two websites for a example of what we are looking for: .
http://www.brazecouncil.example/
http://www.lodning.example/
The newsletter has to have a similar theme as the website and will be used with MS Publisher.

Target Market(s)

Welding association members, welding and metalworking industry, suppliers in welding industry, International welding community, other national welding associations, welding education community

Industry/Entity Type

Welding

Number of Pages Required

3 page

Requirements
Must have
• The RÞKL logo
• Icelandic letters
• email formpage
• Advertisement space/banners/buttons
• Easy to manage
• Compatible with Wordpress
Nice to have
• Welding pictures
• Nice graphics
Should not have
• Should not be dark and heavy set.

```html
<!DOCTYPE html>
<html lang="is">
<head>
<meta charset="utf-8">
<title>RÞKL – Smiðjufélag Norðurs</title>
<link rel="stylesheet" href="https://fonts.googleapis.com/css2?family=Arimo:wght@400;700&family=Questrial&family=Teko:wght@400&display=swap">
<style>
:root{
  --red:#d91b24;
  --teal:#134a63;
  --teal-text:#0f5068;
  --sky:#d3f0fb;
  --grey-box:#ebebeb;
  --ink:#222;
  --muted:#777;
  --white:#fff;
}
*{margin:0;padding:0;box-sizing:border-box}
html,body{width:1200px;height:2320px;overflow:hidden;background:var(--white)}
body{position:relative;font-family:"Arimo",Arial,sans-serif;color:var(--ink)}
.abs{position:absolute}

/* hero */
.hero{left:0;top:0;width:1200px;height:638px;background:radial-gradient(circle at 52% 62%,#f6e6c4 0,#d8913b 12%,#4d4a66 32%,#23315c 60%,#1a1d2a 100%)}
.site-header{left:100px;top:0;width:1001px;height:135px;background:rgba(255,255,255,.95);box-shadow:0 2px 6px rgba(0,0,0,.2)}
.brand{left:20px;top:36px;display:flex;align-items:center;gap:10px}
.brand-dot{width:22px;height:22px;border-radius:50%;background:var(--red)}
.brand-name{font-family:"Questrial",sans-serif;font-size:40px;color:var(--red);letter-spacing:1px}
.contact{right:20px;top:42px;display:flex;gap:22px;font-size:14px;color:#333;align-items:center}
.contact span{display:flex;align-items:center;gap:10px}
.main-nav{left:376px;top:94px;display:flex;font-size:13px;color:#333}
.main-nav a{color:inherit;text-decoration:none;position:absolute;white-space:nowrap}
.nav-active::after{content:"";position:absolute;left:-20px;right:-20px;top:29px;height:5px;background:var(--red)}

/* finder */
.finder{left:0;top:638px;width:1200px;height:116px;background:var(--red)}
.finder-label{left:330px;top:46px;color:var(--white);font-size:19px;letter-spacing:1px}
.finder-input{left:425px;top:42px;width:388px;height:34px;background:var(--white);border:none}
.finder-go{left:818px;top:42px;width:88px;height:34px;background:var(--teal);color:var(--white);font-size:21px;text-align:center;line-height:36px}

/* about */
.about{left:0;top:754px;width:1200px;height:357px;background:var(--sky)}
.about h1{position:absolute;left:120px;top:40px;font-family:"Questrial",sans-serif;font-weight:400;font-size:46px;color:var(--teal-text)}
.about p{position:absolute;left:120px;top:114px;width:985px;font-size:13.5px;line-height:24px;color:#333}
.about .lead{top:256px;font-weight:700;font-size:12.5px;color:var(--teal-text)}

/* section titles */
.section-title{font-family:"Questrial",sans-serif;font-size:44px;color:var(--teal-text);text-align:center;display:flex;align-items:center;justify-content:center;gap:22px}
.rule{display:block;height:14px;border-top:1px solid #c9c9c9;border-bottom:1px solid #c9c9c9;position:relative}
.rule::after{content:"";position:absolute;left:0;right:0;top:5px;border-top:1px solid #c9c9c9}

/* services */
.services-title{left:130px;top:1162px;width:933px}
.service{top:1265px;width:284px}
.service-photo{width:284px;height:140px}
.service h3{font-family:"Questrial",sans-serif;font-weight:400;font-size:24px;color:var(--red);text-align:center;margin-top:20px}
.service p{background:var(--grey-box);margin-top:12px;height:153px;padding:22px 10px 0;font-size:14px;line-height:20px;color:#222}

/* news */
.news{left:0;top:1727px;width:1200px;height:341px;background:var(--sky)}
.news-title{position:absolute;left:120px;top:30px;width:955px;font-size:36px}
.news-item{position:absolute;top:128px;width:420px}
.news-num{position:absolute;left:0;top:0;width:46px;height:42px;background:var(--white);border:1px solid #d5d5d5;color:var(--red);font-family:"Questrial",sans-serif;font-size:24px;text-align:center;line-height:40px}
.news-body{position:absolute;left:58px;top:0;width:362px}
.news-body h4{font-size:13px;font-weight:700;line-height:19px;color:#222;letter-spacing:.3px}
.news-body p{font-size:11.5px;line-height:19px;color:var(--muted);margin-top:10px}
.news-body a{font-size:12px;font-weight:700;color:#333;text-decoration:none}
.news-divider{position:absolute;left:607px;top:105px;width:1px;height:170px;background:#c3d9e2}

/* footer */
.site-footer{left:0;top:2068px;width:1200px;height:252px;background:var(--teal);border-top:6px solid #a9c3cf}
.footer-h{font-family:"Teko",sans-serif;font-size:34px;color:var(--white);font-weight:400}
.testimonial{left:100px;top:22px;width:320px}
.testimonial p{margin-top:10px;padding-left:24px;font-size:14px;line-height:22px;color:var(--white);position:relative}
.testimonial p::before{content:"\201C";position:absolute;left:0;top:-8px;font-size:34px;color:#9bb6c3;font-family:Georgia,serif}
.testimonial p::after{content:"\201D";font-size:30px;color:#9bb6c3;font-family:Georgia,serif;vertical-align:-10px;margin-left:6px}
.quick-links{left:470px;top:22px}
.quick-links ul{list-style:none;margin-top:10px}
.quick-links li{font-size:13px;color:var(--white);line-height:28px;padding-left:26px;position:relative}
.quick-links li::before{content:"";position:absolute;left:6px;top:12px;width:5px;height:5px;border-radius:50%;background:var(--white)}
.footer-brand{left:806px;top:58px;display:flex;align-items:center;gap:10px}
.footer-brand .brand-name{color:var(--white);font-size:46px}
.footer-brand .brand-dot{background:var(--white)}
.copyright{left:802px;top:204px;font-size:11px;color:var(--white);font-weight:700}
</style>
</head>
<body>

<div class="abs hero" role="img" aria-label="Welder in a protective mask and blue jacket grinding metal, showering orange sparks"></div>

<header class="abs site-header">
  <div class="abs brand"><span class="brand-dot"></span><span class="brand-name">RÞKL</span></div>
  <div class="abs contact">
    <span><svg width="18" height="18" viewBox="0 0 24 24"><path d="M6.6 10.8a15 15 0 0 0 6.6 6.6l2.2-2.2a1 1 0 0 1 1-.25 11.4 11.4 0 0 0 3.6.57 1 1 0 0 1 1 1V20a1 1 0 0 1-1 1A17 17 0 0 1 3 4a1 1 0 0 1 1-1h3.5a1 1 0 0 1 1 1c0 1.25.2 2.45.57 3.57a1 1 0 0 1-.25 1z" fill="#222"/></svg>+ 1 808 555 0147</span>
    <span><svg width="20" height="15" viewBox="0 0 20 15"><rect x="0.5" y="0.5" width="19" height="14" fill="#222"/><path d="M1 1l9 7 9-7" stroke="#fff" stroke-width="1.5" fill="none"/></svg>info@nfgforge.example</span>
  </div>
  <nav class="abs main-nav">
    <a class="nav-active" style="left:0">HOME</a>
    <a style="left:88px">NEWS</a>
    <a style="left:176px">EDUCATION</a>
    <a style="left:302px">LIBRARY</a>
    <a style="left:404px">LOKALAVD</a>
    <a style="left:521px">YOUNG STUD</a>
  </nav>
</header>

<section class="abs finder">
  <div class="abs finder-label">I AM A :</div>
  <div class="abs finder-input"></div>
  <div class="abs finder-go">GO</div>
</section>

<section class="abs about">
  <h1>About RÞKL</h1>
  <p>Lorem Ipsum is simply dummy text of the printing and typesetting industry. Lorem Ipsum has been the industry's standard dummy text ever since the 1500s, when an unknown printer took a galley Ipsum has been the industry's standard dummy text ever since the 1500s, when an unknown printer took a galley of type and scrambled it to make a type specimen book. It has survived not only five centuries, but also the leap into electronic typesetting, remaining of type and scrambled it to make a type specimen book. It has survived not only five centuries, but also the leap into electronic typesetting, remaining essentially unchanged.</p>
  <p class="lead">the industry's standard dummy text ever since the 1500s,</p>
</section>

<h2 class="abs section-title services-title"><span class="rule" style="width:318px"></span>Our Services<span class="rule" style="width:318px"></span></h2>

<article class="abs service" style="left:108px">
  <div class="service-photo" role="img" aria-label="Welder at work in a dark workshop with bright white arc light" style="background:radial-gradient(circle at 45% 65%,#f2f6ff 0,#8fb0d8 18%,#2c3f63 45%,#12151f 100%)"></div>
  <h3>Institutional Investors</h3>
  <p>Take advantage of our great deals on cruise packages.Save time and money with these special discounted offers by Harbor Line Tours.  To reserve your package</p>
</article>
<article class="abs service" style="left:459px">
  <div class="service-photo" role="img" aria-label="Welder in blue workwear cutting steel amid orange sparks" style="background:radial-gradient(circle at 55% 70%,#fff1cf 0,#e59a35 16%,#34426c 45%,#161a28 100%)"></div>
  <h3>Wealthy Individuals</h3>
  <p>Take advantage of our great deals on cruise packages.Save time and money with these special discounted offers by Harbor Line Tours.  To reserve your package</p>
</article>
<article class="abs service" style="left:809px">
  <div class="service-photo" role="img" aria-label="Welder working on a steel beam structure under a blue sky" style="background:linear-gradient(180deg,#2f8fd8 0,#5eaee8 55%,#5a5650 100%)"></div>
  <h3>Family Offices</h3>
  <p>Take advantage of our great deals on cruise packages.Save time and money with these special discounted offers by Harbor Line Tours.  To reserve your package</p>
</article>

<section class="abs news">
  <h2 class="section-title news-title"><span class="rule" style="width:370px"></span>Corporate News<span class="rule" style="width:310px"></span></h2>
  <div class="news-item" style="left:105px">
    <div class="news-num">01</div>
    <div class="news-body">
      <h4>LOREM IPSUM DOLOR SIT AMET CONSECTETUR ADIPISICING</h4>
      <p>Sorrupti quos dolores etquas molestias exceptur sint occaecati cupificia deserunt mollitia animi id est laborum et dolorum fuga. Et harum quidem rerum facilisest et expedita distinctio.Sorrupti quos dolores etquas moles</p>
      <a>read more...</a>
    </div>
  </div>
  <div class="news-divider"></div>
  <div class="news-item" style="left:628px">
    <div class="news-num">02</div>
    <div class="news-body">
      <h4>LOREM IPSUM DOLOR SIT AMET CONSECTETUR ADIPISICING</h4>
      <p>Sorrupti quos dolores etquas molestias exceptur sint occaecati cupificia deserunt mollitia animi id est laborum et dolorum fuga. Et harum quidem rerum facilisest et expedita distinctio.Sorrupti quos dolores etquas moles</p>
      <a>read more...</a>
    </div>
  </div>
</section>

<footer class="abs site-footer">
  <div class="abs testimonial">
    <h3 class="footer-h">Testimonials</h3>
    <p>Video ads are free to create. Only pay to remove the watermark and download in high resolution when you're 100% satisfied with your ad. Once you've bought your ad, use it in the following places to increase sales and conversions</p>
  </div>
  <div class="abs quick-links">
    <h3 class="footer-h">Quick Links</h3>
    <ul>
      <li>HOME</li>
      <li>ABOUT US</li>
      <li>PROPERTIES</li>
      <li>SERVICES &amp; NEWS</li>
      <li>REFERENCES</li>
      <li>CONTACT</li>
    </ul>
  </div>
  <div class="abs footer-brand"><span class="brand-dot"></span><span class="brand-name">RÞKL</span></div>
  <div class="abs copyright">© 2014 RÞKL, ALL RIGHTS RESERVED.</div>
</footer>

</body>
</html>
```